Agency Website & Personal brand

My name is Kostas Vranelis & I've been a digital marketer & an e-commerce expert since 2010.

- I've spoken to 20 different events around the world up to 3,000 people in size.
- I've sold over 1500 training courses around e-commerce growth.
- I have over 100 testimonials (video & photo) from successful students who bought my training
- I have dozens of video testimonials from respected entrepreneurs that vouch for me and my work
- I have photos with marketing legends with that I shared the stage like Owen Tarrick, Martin Fellowbrand, Glen Maro & more
- I am the host of the Aegean Roundtable since 2017 - a high-level networking event for 7 & 8 figure entrepreneurs - 100 people have come to Greece since 2017
- I have tons of videos created where I showcase my expertise on growth
- I have worked with dozens of e-commerce stores on their growth & helped them scale to multiple 6, 7 & 8 figures either on consulting

I need a website design that showcases my authority & be a lead generating machine.

The goal is to bring people on a call with me but also grab their email and start building the relationship with them and free valuable content

We have 3 offers :

1. Paid ads (Done for You)
2. Consulting/Mastermind (Done with You)
3. Training (Do it Yourself)

```html
<!DOCTYPE html>
<html lang="en">
<head>
<meta charset="utf-8">
<title>Kostas Vranelis — Growth Speaker &amp; E-commerce Consultant</title>
<link href="https://fonts.googleapis.com/css2?family=Montserrat+Alternates:wght@400;500;600;700&family=Montserrat:ital,wght@0,400;0,500;0,600;1,400&display=swap" rel="stylesheet">
<style>
:root{
  --blue:#1fa8e1;
  --blue-dark:#1591c6;
  --ink:#1b1d24;
  --text:#4a4d57;
  --muted:#8a8d96;
  --navy:#0b0f1c;
  --navy-2:#141a2c;
  --white:#ffffff;
  --line:#e6e8ec;
  --soft:#eeeff2;
}
*{box-sizing:border-box;margin:0;padding:0}
html,body{width:1200px;height:4435px;overflow:hidden}
body{position:relative;background:var(--white);font-family:"Montserrat",sans-serif;color:var(--text)}
.abs{position:absolute}
.display{font-family:"Montserrat Alternates",sans-serif}
.btn{position:absolute;display:flex;align-items:center;justify-content:center;font-family:"Montserrat Alternates",sans-serif;font-size:11px;font-weight:600;border:2px solid var(--blue);color:var(--ink);background:var(--white)}
.btn.solid{background:var(--blue);color:var(--white)}
.eyebrow{font-family:"Montserrat Alternates",sans-serif;color:var(--blue);font-size:15px}
.photo{position:absolute}

/* header & hero */
.hero{position:absolute;left:0;top:0;width:1200px;height:561px;background:linear-gradient(90deg,#1a1e2b 0%,#23283a 45%,#1e5d8c 70%,#27a7e4 100%)}
.brand{font-family:"Montserrat Alternates",sans-serif;font-weight:700;font-size:19px;color:var(--blue)}
.nav{position:absolute;top:22px;left:472px;display:flex;gap:31px;font-size:11px;font-family:"Montserrat Alternates",sans-serif;color:var(--white)}
.nav .active{color:var(--blue)}
.hero-contact{position:absolute;left:975px;top:15px;width:120px;height:32px;border:2px solid var(--white);color:var(--white);font-size:11px;display:flex;align-items:center;justify-content:center;font-family:"Montserrat Alternates",sans-serif}
.hero h1{position:absolute;left:200px;top:248px;font-family:"Montserrat Alternates",sans-serif;font-weight:500;font-size:46px;color:var(--white)}
.hero h1 b{font-weight:700}

/* about */
.about-block{left:0;top:744px;width:200px;height:200px;background:var(--blue)}
.about h2,.h2{font-family:"Montserrat Alternates",sans-serif;font-weight:400;font-size:24px;line-height:30px;color:var(--ink)}
.h2 b{font-weight:600}
.body-sm{font-size:10px;line-height:19px;color:var(--text)}

/* stats */
.stats{left:0;top:1128px;width:1200px;height:244px;background-image:radial-gradient(#dfe2e8 1px,transparent 1px);background-size:12px 12px}
.stat{position:absolute;top:1180px;display:flex;align-items:flex-end;gap:6px;font-family:"Montserrat Alternates",sans-serif;font-size:12px;color:var(--ink)}
.stat .num{font-size:44px;color:var(--blue);line-height:44px}
.stat-div{position:absolute;top:1155px;width:1px;height:75px;background:var(--line)}

/* services */
.card-cap{position:absolute;width:206px;height:74px;background:var(--white);box-shadow:0 6px 18px rgba(0,0,0,.08);text-align:center;padding-top:20px;font-family:"Montserrat Alternates",sans-serif;font-weight:600;font-size:13px;color:var(--ink)}
.card-cap small{display:block;font-family:"Montserrat",sans-serif;font-weight:400;font-size:9px;color:var(--blue);margin-top:3px}
.card-cap.active{background:var(--blue);color:var(--white)}
.card-cap.active small{color:var(--white)}

/* events */
.events-bg{left:0;top:1929px;width:1200px;height:680px;background:linear-gradient(135deg,#f3f4f6,#e4e6ea 50%,#f1f2f4)}
.tag{position:absolute;height:20px;padding:0 12px;background:var(--blue);color:var(--white);font-size:10px;font-weight:600;display:flex;align-items:center;clip-path:polygon(0 0,88% 0,100% 100%,0 100%)}
.date{position:absolute;font-size:9px;color:var(--blue);text-align:center}
.ev-title{position:absolute;font-family:"Montserrat Alternates",sans-serif;font-size:13px;line-height:17px;color:var(--ink);text-align:center}

/* testimonials */
.quote-card{left:613px;top:2793px;width:386px;height:224px;background:var(--white);box-shadow:0 8px 30px rgba(0,0,0,.1);padding:26px 24px}
.arrow-btn{position:absolute;width:30px;height:30px;border:2px solid var(--blue);display:flex;align-items:center;justify-content:center;background:var(--white)}

/* cta band */
.band{left:0;top:3179px;width:1200px;height:186px;background:var(--blue)}

/* footer */
.footer{left:0;top:4107px;width:1200px;height:328px;background:var(--navy)}
.foot-h{font-family:"Montserrat Alternates",sans-serif;font-size:13px;color:var(--white)}
.foot-link{font-size:10px;color:#c9ccd4;line-height:22px}
.social{position:absolute;width:28px;height:28px;border-radius:50%;border:1px solid var(--blue)}
</style>
</head>
<body>

<!-- HERO -->
<header class="hero">
  <div class="photo" role="img" aria-label="Speaker on a stage with audience in the foreground" style="left:0;top:0;width:1200px;height:561px;background:linear-gradient(90deg,rgba(15,18,28,.6),rgba(15,18,28,.2) 60%,rgba(0,0,0,0))"></div>
  <div class="brand abs" style="left:105px;top:20px">Kostas Vranelis</div>
  <nav class="nav">
    <span class="active">Home</span><span>About me</span><span>Services</span><span>Events</span><span>Gallery</span><span>Testimonials</span>
  </nav>
  <div class="hero-contact">Contact us</div>
  <div class="eyebrow abs" style="left:200px;top:214px;font-size:19px">Hello, i'm</div>
  <h1>Kostas <b>Vranelis</b></h1>
  <p class="abs" style="left:200px;top:314px;width:400px;font-size:12px;line-height:18px;color:var(--white)">Lorem ipsum is simply dummy text of the printing working typesetting industry.</p>
  <div class="btn" style="left:200px;top:377px;width:118px;height:31px;border-color:var(--white)">Contact us</div>
</header>

<!-- ABOUT -->
<section class="about">
  <div class="abs about-block"></div>
  <div class="photo" role="img" aria-label="Speaker presenting in a conference room" style="left:200px;top:625px;width:325px;height:437px;background:linear-gradient(180deg,#8d8a82,#5b564f 60%,#3b3a37)"></div>
  <div class="eyebrow abs" style="left:612px;top:676px">About me</div>
  <h2 class="abs" style="left:612px;top:703px;width:360px">Contrary to <b style="font-weight:600">popular belief,</b><br><b style="font-weight:600">Lorem ipsum</b> is not simply<br>random text.</h2>
  <p class="abs body-sm" style="left:612px;top:804px;width:390px">Lorem Ipsum is simply dummy text of the printing and typesetting industry. Lorem Ipsum has been the industry's standard dummy text ever since the 1500s, when an unknown printer took a galley of type and scrambled it to make a type specimen book.</p>
  <p class="abs body-sm" style="left:612px;top:898px;width:390px">It has survived not only five centuries, but also the leap into electronic typesetting, remaining essentially unchanged. It was popularised in the 1960s with the release of Letraset sheets containing</p>
  <div class="btn" style="left:612px;top:979px;width:120px;height:31px">Explore more</div>
  <div class="btn solid" style="left:742px;top:979px;width:118px;height:31px">Consult now</div>
</section>

<!-- STATS -->
<section>
  <div class="abs stats"></div>
  <div class="stat" style="left:218px"><span>Sold over</span><span class="num">1500</span><span>training</span></div>
  <div class="abs display" style="left:299px;top:1226px;font-size:12px;color:var(--ink)">courses</div>
  <div class="stat-div" style="left:464px"></div>
  <div class="stat" style="left:507px"><span>Over</span><span class="num">100</span><span>testimonials</span></div>
  <div class="stat-div" style="left:737px"></div>
  <div class="stat" style="left:780px"><span>Over</span><span class="num">20</span><span>Different events</span></div>
  <div class="abs display" style="left:818px;top:1226px;font-size:12px;color:var(--ink)">around the world</div>
  <div class="btn" style="left:541px;top:1279px;width:118px;height:30px">Contact now</div>
</section>

<!-- SERVICES -->
<section>
  <div class="eyebrow abs" style="left:0;width:1200px;text-align:center;top:1431px;font-size:14px">Services</div>
  <div class="h2 abs" style="left:0;width:1200px;text-align:center;top:1452px">We have <b>3 offers</b></div>
  <div class="photo" role="img" aria-label="Two people in VR headsets seated back to back" style="left:200px;top:1507px;width:250px;height:249px;background:linear-gradient(160deg,#b9b7b2,#7c7a76)"></div>
  <div class="photo" role="img" aria-label="Business handshake across a meeting table" style="left:475px;top:1507px;width:250px;height:249px;background:linear-gradient(160deg,#c8c4bd,#6f6c68)"></div>
  <div class="photo" role="img" aria-label="Trainer presenting to a small team at a flipchart" style="left:750px;top:1507px;width:250px;height:249px;background:linear-gradient(160deg,#d6d6d4,#7e7f82)"></div>
  <div class="card-cap" style="left:222px;top:1729px">Paid ads<small>Done for You</small></div>
  <div class="card-cap active" style="left:497px;top:1729px">Consulting/Mastermind<small>Done with You</small></div>
  <div class="card-cap" style="left:772px;top:1729px">Training<small>Do it Yourself</small></div>
  <div class="btn" style="left:541px;top:1836px;width:118px;height:30px">Consult now</div>
</section>

<!-- EVENTS -->
<section>
  <div class="abs events-bg"></div>
  <div class="abs display" style="left:269px;width:387px;text-align:center;top:1986px;font-size:22px;color:var(--ink)">Events</div>
  <div class="photo" role="img" aria-label="Q&amp;A stage session with speaker and moderator" style="left:269px;top:2044px;width:387px;height:281px;background:linear-gradient(180deg,#1a1a1c 0%,#2a2a2a 30%,#e8d35a 55%,#d9c24a 85%,#f4f4f4 100%)"></div>
  <div class="tag" style="left:269px;top:2304px">Upcoming</div>
  <div class="date" style="left:269px;width:387px;top:2349px">Mar 2, 2023</div>
  <div class="ev-title" style="left:330px;width:265px;top:2374px">Contrary to popular belief, lorem simply random text.</div>
  <p class="abs" style="left:269px;width:387px;top:2421px;font-size:9px;line-height:15px;text-align:center;color:var(--text)">Contrary to popular belief, lorem Ipsum is not simply random text.<br>It has roots in a piece of classical Latin literature</p>
  <div class="abs" style="left:269px;width:387px;top:2466px;font-size:10px;font-weight:600;text-align:center;color:var(--ink)">Read more</div>

  <div class="photo" role="img" aria-label="Video interview recorded in a studio office" style="left:682px;top:1992px;width:250px;height:155px;background:linear-gradient(160deg,#d5d8de,#5b6068)"></div>
  <div class="tag" style="left:682px;top:2125px">Post Event</div>
  <div class="date" style="left:682px;width:250px;top:2165px">Mar 2, 2023</div>
  <div class="ev-title" style="left:682px;width:250px;top:2184px">Contrary to popular belief, lorem simply text.</div>

  <div class="photo" role="img" aria-label="Speaker at a microphone with a green event banner behind" style="left:682px;top:2252px;width:250px;height:155px;background:linear-gradient(160deg,#2a9a5a,#5f6460 60%,#d9d9d9)"></div>
  <div class="tag" style="left:682px;top:2386px">Post Event</div>
  <div class="date" style="left:682px;width:250px;top:2426px">Mar 2, 2023</div>
  <div class="ev-title" style="left:682px;width:250px;top:2445px">Contrary to popular belief, lorem simply text.</div>

  <div class="btn solid" style="left:534px;top:2518px;width:132px;height:30px;border-color:var(--white)">View all events</div>
</section>

<!-- TESTIMONIALS -->
<section>
  <div class="photo" role="img" aria-label="Video testimonial from a smiling client" style="left:200px;top:2672px;width:525px;height:443px;background:linear-gradient(160deg,#8f8a84,#6e6a66 50%,#9b938c)"></div>
  <svg class="abs" style="left:443px;top:2874px" width="38" height="38" viewBox="0 0 38 38" aria-hidden="true"><circle cx="19" cy="19" r="17" fill="none" stroke="#fff" stroke-width="2.5"/><path d="M15 11 L27 19 L15 27 Z" fill="#fff"/></svg>
  <div class="eyebrow abs" style="left:749px;top:2703px">Testimonials</div>
  <div class="h2 abs" style="left:749px;top:2730px">What our <b>clients say</b></div>
  <div class="abs quote-card">
    <div style="display:flex;align-items:center;gap:12px">
      <div role="img" aria-label="Client portrait" style="width:44px;height:44px;border-radius:50%;background:linear-gradient(135deg,#c89a7a,#8a6048)"></div>
      <div><div class="display" style="font-size:12px;font-weight:600;color:var(--ink)">Standard Chunk</div><div style="font-size:8px;color:var(--muted);margin-top:3px">Lorem Ipsum Family</div></div>
    </div>
    <p style="margin-top:16px;font-size:10px;line-height:19px;font-style:italic;color:var(--text)">"There are many variations of passages of Lorem Ipsum available, but the majority have suffered alteration in some form, by injected humour, or randomised words which don't look even slightly believable. If you are going to use a passage lorem Ipsum, you hidden in the middle of text. all the Lorem Ipsum generators Internet tend to repeat."</p>
  </div>
  <div class="arrow-btn" style="left:749px;top:3049px"><svg width="8" height="10" viewBox="0 0 8 10"><path d="M6 1 L2 5 L6 9" fill="none" stroke="#1b1d24" stroke-width="1.5"/></svg></div>
  <div class="btn" style="left:796px;top:3049px;width:156px;height:30px">View all reviews</div>
  <div class="arrow-btn" style="left:969px;top:3049px"><svg width="8" height="10" viewBox="0 0 8 10"><path d="M2 1 L6 5 L2 9" fill="none" stroke="#1b1d24" stroke-width="1.5"/></svg></div>
</section>

<!-- CTA BAND -->
<section>
  <div class="abs band"></div>
  <div class="photo" role="img" aria-label="Speaker standing on a seaside cliff" style="left:796px;top:3179px;width:404px;height:186px;clip-path:polygon(42% 0,100% 0,100% 100%,0 100%);background:linear-gradient(160deg,#9fc2d8,#5a7a5a 55%,#4b5a3c)"></div>
  <p class="abs display" style="left:200px;top:3229px;width:580px;font-size:22px;line-height:27px;color:var(--white)">I have worked with dozens of <b style="font-weight:700">e-commerce stores on their growth &amp; helped them</b> scale to multiple 6, 7 &amp; 8 figures either on consulting.</p>
  <div class="btn" style="left:862px;top:3256px;width:137px;height:31px;border-color:var(--white)">Consult now!</div>
</section>

<!-- GALLERY -->
<section>
  <div class="h2 abs" style="left:0;width:1200px;text-align:center;top:3424px">Event <b>gallery</b></div>
  <div class="photo" role="img" aria-label="Speaker working at a desk with monitors" style="left:200px;top:3513px;width:218px;height:218px;background:linear-gradient(160deg,#b8b6b2,#6a645c)"></div>
  <div class="photo" role="img" aria-label="Crowd in a lit city square at night, video" style="left:444px;top:3482px;width:312px;height:281px;background:linear-gradient(180deg,#3b3f4a,#6a3a3a 40%,#2a2a30)"></div>
  <svg class="abs" style="left:580px;top:3603px" width="40" height="40" viewBox="0 0 40 40" aria-hidden="true"><circle cx="20" cy="20" r="18" fill="none" stroke="#fff" stroke-width="2.5"/><path d="M16 12 L28 20 L16 28 Z" fill="#fff"/></svg>
  <div class="photo" role="img" aria-label="Band performing on a purple-lit stage" style="left:780px;top:3513px;width:219px;height:218px;background:linear-gradient(160deg,#5a2a8a,#c23aa0 50%,#2a1a4a)"></div>
  <div class="arrow-btn" style="left:185px;top:3607px;width:28px;height:28px"><svg width="8" height="10" viewBox="0 0 8 10"><path d="M6 1 L2 5 L6 9" fill="none" stroke="#1b1d24" stroke-width="1.5"/></svg></div>
  <div class="arrow-btn" style="left:986px;top:3607px;width:28px;height:28px"><svg width="8" height="10" viewBox="0 0 8 10"><path d="M2 1 L6 5 L2 9" fill="none" stroke="#1b1d24" stroke-width="1.5"/></svg></div>
  <div class="btn" style="left:550px;top:3795px;width:100px;height:30px">View all</div>
</section>

<!-- NEWSLETTER -->
<section>
  <div class="abs" style="left:0;top:3883px;width:1200px;height:224px;background-image:radial-gradient(#e4e6ea 1px,transparent 1px);background-size:12px 12px"></div>
  <div class="h2 abs" style="left:200px;top:3952px">Sign up for <b>newsletter</b></div>
  <p class="abs" style="left:200px;top:3995px;width:320px;font-size:12px;line-height:20px;color:var(--text)">To know more about an eCommerce growth to multiple 6, 7 &amp; 8 figures <b style="color:var(--ink)">Sign Up Now!</b></p>
  <div class="abs" style="left:611px;top:3981px;width:290px;height:35px;border:1px solid #9a9da5;background:var(--white);font-size:9px;color:var(--text);padding:11px 16px">Enter your email ...</div>
  <div class="btn solid" style="left:899px;top:3981px;width:100px;height:35px">Submit</div>
</section>

<!-- FOOTER -->
<footer class="abs footer">
  <div class="abs display" style="left:200px;top:65px;font-size:27px;font-weight:700;color:var(--blue)">Kostas Vranelis</div>
  <div class="social" style="left:254px;top:122px" aria-label="Social link"></div>
  <div class="social" style="left:293px;top:122px;background:var(--blue)" aria-label="Social link"></div>
  <div class="social" style="left:330px;top:122px" aria-label="Social link"></div>

  <div class="abs foot-h" style="left:513px;top:67px">Contact us</div>
  <svg class="abs" style="left:513px;top:100px" width="10" height="10" viewBox="0 0 10 10"><path d="M2 1 L4 1 L5 3 L4 4 Q5 6 6 6 L7 5 L9 6 L9 8 Q8 9 6 8.5 Q2 7 1 3 Q1 1.5 2 1Z" fill="var(--blue)"/></svg>
  <div class="abs" style="left:535px;top:98px;font-size:13px;color:var(--white)">123 456 7890</div>
  <svg class="abs" style="left:513px;top:130px" width="10" height="8" viewBox="0 0 10 8"><rect x=".5" y=".5" width="9" height="7" fill="none" stroke="var(--blue)"/><path d="M.5 .5 L5 4.5 L9.5 .5" fill="none" stroke="var(--blue)"/></svg>
  <div class="abs" style="left:535px;top:128px;font-size:10px;color:#c9ccd4">info@kostasvranelis.com</div>
  <svg class="abs" style="left:514px;top:154px" width="8" height="11" viewBox="0 0 8 11"><path d="M4 10.5 Q0 6 0 4 A4 4 0 0 1 8 4 Q8 6 4 10.5Z" fill="var(--blue)"/><circle cx="4" cy="4" r="1.4" fill="var(--navy)"/></svg>
  <div class="abs" style="left:535px;top:152px;font-size:10px;color:var(--blue)">Kostas Vranelis</div>
  <div class="abs" style="left:535px;top:166px;width:220px;font-size:10px;line-height:14px;color:#c9ccd4">1100 Lorem. ipsum dr. ste 107 siteamet, CA 12345</div>

  <div class="abs foot-h" style="left:800px;top:67px">Quick links</div>
  <div class="abs foot-link" style="left:800px;top:96px">Home<br>About me<br>Services<br>Events<br>Gallery</div>
  <div class="abs foot-link" style="left:889px;top:96px">Testimonials<br>Contact Us</div>

  <svg class="abs" style="left:1093px;top:67px" width="20" height="24" viewBox="0 0 20 24" aria-hidden="true"><path d="M10 0 L20 24 L10 18 L0 24 Z" fill="var(--blue)"/></svg>

  <div class="abs" style="left:0;top:263px;width:1200px;height:1px;background:var(--navy-2)"></div>
  <div class="abs" style="left:0;top:290px;width:1200px;text-align:center;font-size:9px;color:#c9ccd4">2023 <span style="color:var(--blue)">Kostas Vranelis</span>. All Rights Reserved.</div>
</footer>

</body>
</html>
```